Business Card Design Project

it should have the logo in one side
the other side

Name
Position
telephone
email

Target Market(s)

Business prospects and upscale Fashion shoppers

Industry/Entity Type

Business

Font styles to use
Serif
Sans Serif

Requirements
Must have
• very elegant, upscale, modern
Nice to have
• layering, embossed
Should not have
• Should not use any color OTHER THAN black, silver, white or purple

```html
<!DOCTYPE html>
<html lang="en">
<head>
<meta charset="utf-8">
<title>Norhaven Business Card</title>
<link rel="stylesheet" href="https://fonts.googleapis.com/css2?family=Cormorant+Garamond:wght@400;500;600&display=swap">
<style>
  :root {
    --page-bg: #ffffff;
    --card-black: #121212;
    --card-edge: #050505;
    --silver-light: #f0f0f0;
    --silver: #bdbdbd;
    --silver-dark: #6f6f6f;
    --text-white: #e6e6e6;
    --text-muted: #a8a8a8;
  }
  * { margin: 0; padding: 0; box-sizing: border-box; }
  html, body {
    width: 1200px;
    height: 900px;
    overflow: hidden;
    background: var(--page-bg);
  }
  .canvas {
    width: 1200px;
    height: 900px;
    display: flex;
    align-items: center;
    justify-content: center;
    gap: 50px;
  }
  .card {
    width: 530px;
    height: 300px;
    border-radius: 26px;
    background: radial-gradient(ellipse at 50% 45%, #262626 0%, var(--card-black) 70%, #0a0a0a 100%);
    position: relative;
    overflow: hidden;
    box-shadow: 0 14px 24px rgba(0, 0, 0, 0.18);
  }
  .card--front {
    background: var(--card-edge);
    padding: 9px;
  }
  .front-frame {
    width: 100%;
    height: 100%;
    border-radius: 20px;
    padding: 6px;
    background: linear-gradient(180deg, var(--silver-light) 0%, var(--silver) 50%, var(--silver-dark) 100%);
  }
  .front-panel {
    width: 100%;
    height: 100%;
    border-radius: 15px;
    background: radial-gradient(ellipse at 40% 45%, #2a2a2a 0%, #151515 60%, #0c0c0c 100%);
    display: flex;
    align-items: center;
    justify-content: flex-start;
    padding-left: 120px;
  }
  .brand-name {
    font-family: "Cormorant Garamond", serif;
    font-weight: 600;
    font-size: 40px;
    letter-spacing: 5px;
    color: var(--silver);
    text-transform: uppercase;
  }
  .back-texture {
    position: absolute;
    inset: 0;
    background: radial-gradient(ellipse at 50% 50%, rgba(60, 60, 60, 0.45) 0%, rgba(30, 30, 30, 0.2) 45%, rgba(0, 0, 0, 0) 75%);
  }
  .contact {
    position: relative;
    height: 100%;
    display: flex;
    flex-direction: column;
    align-items: center;
    justify-content: center;
    font-family: "Cormorant Garamond", serif;
    text-align: center;
  }
  .contact__name {
    font-size: 26px;
    font-weight: 500;
    color: var(--silver);
    line-height: 1.1;
  }
  .contact__role {
    font-size: 12px;
    color: var(--text-muted);
    margin-bottom: 30px;
  }
  .contact__line {
    font-size: 16px;
    color: var(--text-white);
    line-height: 1.25;
  }
</style>
</head>
<body>
  <main class="canvas">
    <section class="card card--front" aria-label="Card front">
      <div class="front-frame">
        <div class="front-panel">
          <span class="brand-name">Norhaven</span>
        </div>
      </div>
    </section>

    <section class="card card--back" aria-label="Card back">
      <div class="back-texture" role="img" aria-label="Faint tonal diamond pattern on black"></div>
      <div class="contact">
        <p class="contact__name">Miles Carver</p>
        <p class="contact__role">Manager</p>
        <p class="contact__line">+61 (0) 400 118 274</p>
        <p class="contact__line">milescarver@mail.com</p>
      </div>
    </section>
  </main>
</body>
</html>
```